Website design for KOVIL – data platform for healthcare & social housing

We’re looking for a clean, modern multi-page website design for KOVIL — a data platform for healthcare and social housing.

📎 Please read the attached PDF for full structure, context, and design guidance.
The briefing is essential to understanding this project.

➡️ For the initial submission, only the homepage design (including header and footer) is required.

This will help us assess design direction and fit.

The full project includes four levels (homepage, general page, product overview, and product detail), which will be completed after selecting the final designer.

Industry/Entity Type

data platform for healthcare & social housing

Number of Pages Required

1 page

Font styles to use
Sans Serif

Requirements
Must have
• Please read the attached PDF
Nice to have
Should not have

```html
<!DOCTYPE html>
<html lang="en">
<head>
<meta charset="utf-8">
<title>KOVIL – Data Analytics for Healthcare and Social Housing</title>
<link rel="stylesheet" href="https://fonts.googleapis.com/css2?family=Lexend:wght@400;500;600&family=Montserrat:wght@400;500;600;700&display=swap">
<style>
:root{
  --navy:#0f2f6e;
  --blue:#1b4c9b;
  --blue-deep:#123d85;
  --orange:#f47a12;
  --text:#2b2f3a;
  --muted:#555c6b;
  --card:#ffffff;
  --line:#d7dbe4;
}
*{box-sizing:border-box;margin:0;padding:0}
html,body{width:1200px;height:4906px;overflow:hidden}
body{position:relative;font-family:"Montserrat",sans-serif;color:var(--text);
  background:linear-gradient(180deg,#fff6ee 0,#ffffff 700px,#ffffff 2900px,#fff4ea 3150px,#ffffff 3600px);}
.abs{position:absolute}
h1,h2,h3,.heading{font-family:"Lexend",sans-serif;color:var(--navy);font-weight:500}
.btn{position:absolute;display:flex;align-items:center;justify-content:center;border-radius:20px;font-size:13px;font-weight:600;height:38px}
.btn-orange{background:var(--orange);color:#fff}
.btn-outline{border:1.5px solid var(--blue);color:var(--navy);background:#fff}
.btn-white{background:#fff;color:var(--navy)}
.btn-outline-light{border:1.5px solid #fff;color:#fff}
.eyebrow{position:absolute;font-size:13px;font-weight:600;color:var(--blue)}
.center{left:0;width:1200px;text-align:center}

/* header */
.logo{font-family:"Lexend",sans-serif;font-weight:500;color:var(--blue);font-size:28px;letter-spacing:6px}
.nav{left:232px;top:33px;display:flex;gap:31px;font-size:12px;color:var(--navy)}
/* hero */
.hero-photo{position:absolute;left:571px;top:0;width:629px;height:667px;
  clip-path:polygon(0 64%,52% 0,100% 0,100% 36%,62% 92%,38% 100%,12% 92%);
  background:linear-gradient(135deg,#b9d9ea,#3f87b3 45%,#1a5684 80%,#0f2f5a)}
.hero-title{left:141px;top:158px;font-size:39px;line-height:54px;width:430px}
.feature-bar{left:103px;top:530px;width:992px;height:81px;border-radius:41px;background:var(--orange);
  display:flex;align-items:center;justify-content:center;gap:42px;color:#fff;font-size:13px;font-weight:500}
.feature-bar span{display:flex;align-items:center;gap:8px}

/* help cards */
.help-card{position:absolute;top:926px;width:280px;height:204px;background:var(--card);border-radius:6px;box-shadow:0 6px 24px rgba(20,40,90,.1)}
.help-card .ico{position:absolute;left:42px;top:-28px;width:60px;height:60px;border-radius:50%;background:var(--blue-deep);border:5px solid #dfe6f4;display:flex;align-items:center;justify-content:center}
.help-card h3{position:absolute;left:33px;top:65px;font-size:15px;color:#1d2434}
.help-card p{position:absolute;left:33px;top:105px;width:220px;font-size:12px;line-height:22px;color:var(--muted)}

.round-photo{position:absolute;border-radius:50%;border:10px solid #fff;box-shadow:0 10px 40px rgba(20,40,90,.15)}

/* products */
.product{position:absolute;width:438px;height:383px;background:#fff;border-radius:6px;box-shadow:0 6px 24px rgba(20,40,90,.1);overflow:hidden}
.product .img{height:230px}
.product h3{position:absolute;left:30px;top:258px;font-size:15px;color:#1d2434}
.product p{position:absolute;left:30px;top:290px;width:385px;font-size:12px;line-height:22px;color:var(--muted)}
.product a{position:absolute;left:30px;top:342px;font-size:12px;font-weight:600;color:var(--orange);text-decoration:underline}

.band{position:absolute;left:103px;width:992px;border-radius:140px}

.check{position:absolute;display:flex;align-items:center;gap:10px;font-size:13px;font-weight:600;color:#1d2434}
.check i{width:19px;height:19px;border-radius:50%;background:var(--blue);display:flex;align-items:center;justify-content:center}

/* testimonials */
.quote{position:absolute;top:3785px;width:373px;height:263px;background:#fff;box-shadow:0 6px 24px rgba(20,40,90,.1);padding:30px 28px;font-size:12.5px;line-height:24px;color:var(--muted)}
.quote .who{position:absolute;left:28px;font-size:11px;color:var(--muted)}
.quote .org{position:absolute;left:28px;font-size:14px;font-weight:600;color:#1d2434}
.quote .mark{position:absolute;right:30px;width:44px;height:44px;border-radius:50%;display:flex;align-items:center;justify-content:center;color:#fff;font-family:"Lexend",sans-serif;font-size:30px;line-height:1;padding-top:10px}

/* footer */
.footer{left:0;top:4534px;width:1200px;height:372px;background:linear-gradient(120deg,#1a4a98,#163f86 60%,#1a4fa2)}
.footer h4{position:absolute;font-family:"Lexend",sans-serif;font-weight:500;font-size:15px;color:#fff}
.footer ul{position:absolute;list-style:none;font-size:12px;line-height:26px;color:#fff}
.copyright{position:absolute;left:0;width:1200px;height:40px;border-top:1px solid rgba(255,255,255,.25);color:#fff;font-size:11.5px}
</style>
</head>
<body>

<!-- hero image (placed first so header and text sit above it) -->
<div class="hero-photo" role="img" aria-label="Hands typing on a laptop overlaid with glowing healthcare icons"></div>

<!-- header -->
<div class="abs logo" style="left:63px;top:22px">KOVIL</div>
<nav class="abs nav">
  <span>What is KOVIL?</span><span>Products</span><span>Who it's for</span><span>Community</span><span>About us</span><span>Contact</span>
</nav>
<div class="btn btn-white" style="left:862px;top:22px;width:132px">Plan a Demo</div>
<div class="btn btn-orange" style="left:1003px;top:22px;width:132px">Start KOVIL</div>

<!-- hero -->
<h1 class="abs hero-title">More Impact With Better Control Over Data</h1>
<p class="abs" style="left:141px;top:342px;font-size:13.5px;font-weight:500;color:var(--navy)">Data Analytics For Healthcare And Social Housing</p>
<div class="btn btn-orange" style="left:141px;top:393px;width:134px">Products</div>
<div class="btn btn-outline" style="left:288px;top:393px;width:156px">Plan a Demo</div>

<div class="abs feature-bar">
  <span><svg width="18" height="18" viewBox="0 0 24 24" fill="none" stroke="#fff" stroke-width="2"><rect x="5" y="10" width="14" height="11" rx="2"/><path d="M8 10V7a4 4 0 0 1 8 0v3"/></svg>Secure, Compliant Data Handling</span>
  <span><svg width="18" height="18" viewBox="0 0 24 24" fill="none" stroke="#fff" stroke-width="2"><circle cx="12" cy="12" r="9"/><path d="M12 7v5l3 2"/></svg>Real-Time Insights &amp; Dashboards</span>
  <span><svg width="20" height="18" viewBox="0 0 24 24" fill="none" stroke="#fff" stroke-width="2"><path d="M2 9l5 1 5 4 5-4 5-1M7 10l5 8 5-8"/></svg>Built with Experts in Health &amp; Housing</span>
</div>

<!-- how it helps -->
<div class="eyebrow center" style="top:746px">How KOVIL Helps</div>
<h2 class="abs center" style="top:772px;font-size:30px;line-height:43px">Transforming Data Into Impact For Healthcare<br>&amp; Social Housing</h2>

<div class="help-card" style="left:141px">
  <div class="ico"><svg width="24" height="24" viewBox="0 0 24 24" fill="none" stroke="#fff" stroke-width="1.8"><rect x="3" y="5" width="18" height="13" rx="1"/><path d="M7 14v-3M11 14V9M15 14v-5"/></svg></div>
  <h3>Platform &amp; Products</h3>
  <p>KOVIL provides a robust platform with tailored products for diverse industry needs.</p>
</div>
<div class="help-card" style="left:460px">
  <div class="ico"><svg width="24" height="24" viewBox="0 0 24 24" fill="none" stroke="#fff" stroke-width="1.8"><circle cx="12" cy="7" r="3"/><circle cx="5" cy="10" r="2"/><circle cx="19" cy="10" r="2"/><path d="M6 20v-3a6 6 0 0 1 12 0v3"/></svg></div>
  <h3>Community</h3>
  <p>KOVIL builds a collaborative community for networking and knowledge-sharing.</p>
</div>
<div class="help-card" style="left:779px">
  <div class="ico"><svg width="24" height="24" viewBox="0 0 24 24" fill="none" stroke="#fff" stroke-width="1.8"><circle cx="12" cy="12" r="4"/><path d="M12 2v4M12 18v4M2 12h4M18 12h4"/></svg></div>
  <h3>BI-as-a-Service</h3>
  <p>KOVIL offers BI-as-a-Service, enabling data-driven insights and decision-making.</p>
</div>

<!-- about -->
<div class="round-photo" style="left:133px;top:1229px;width:480px;height:480px;background:linear-gradient(135deg,#e9eef3,#9fb0c0 45%,#3c4a55 75%,#1d2a22)" role="img" aria-label="Analyst pointing at a monitor full of green data columns"></div>
<div class="eyebrow" style="left:671px;top:1276px">ABOUT US</div>
<h2 class="abs" style="left:671px;top:1300px;font-size:30px;line-height:43px;width:400px">Built For Impact. Backed<br>By Data.</h2>
<p class="abs" style="left:671px;top:1408px;width:400px;font-size:12px;line-height:22.5px;color:var(--muted)">At KOVIL, we believe data should drive meaningful change not just reports. Our platform bridges the gap between complex datasets and real-world outcomes in healthcare and social housing. Built by specialists, KOVIL delivers precision analytics and intuitive tools that help professionals act faster and smarter. We collaborate with public and private organizations to ensure our solutions are both robust and relevant. With KOVIL, better data isn't just accessible — it's actionable.</p>
<div class="btn btn-orange" style="left:671px;top:1623px;width:152px">Learn More</div>

<!-- products -->
<div class="eyebrow center" style="top:1815px">Our Products</div>
<h2 class="abs center" style="top:1840px;font-size:30px">Turn Data Into Decisions With KOVIL's Smart Tools</h2>

<div class="product" style="left:143px;top:1922px">
  <div class="img" role="img" aria-label="Laptop with a glowing data security interface" style="background:linear-gradient(135deg,#0b2a4a,#1e6aa8 55%,#6cc4ea)"></div>
  <h3>Public Data Access</h3>
  <p>Access curated &amp; ready-to-use public datasets across sectors, saving hours of research and preparation.</p>
  <a>More Info.</a>
</div>
<div class="product" style="left:623px;top:1922px">
  <div class="img" role="img" aria-label="City skyline connected by a network of data lines" style="background:linear-gradient(180deg,#1b5d8c,#3f8fb8 50%,#0d2f4a)"></div>
  <h3>Climate Risk Scan</h3>
  <p>Assess geographic and asset-level exposure to climate-related risks using intuitive, location-based analytics.</p>
  <a>More Info.</a>
</div>
<div class="product" style="left:143px;top:2347px">
  <div class="img" role="img" aria-label="Tablet showing colourful pricing package options" style="background:linear-gradient(135deg,#e8e8e6,#c9ccd0 50%,#f2a23c 70%,#d9dde2)"></div>
  <h3>Pricing Benchmark</h3>
  <p>Compare prices across suppliers, regions, or time to identify savings opportunities and stay market-aligned.</p>
  <a>More Info.</a>
</div>
<div class="product" style="left:623px;top:2347px">
  <div class="img" role="img" aria-label="Doctor in a white coat holding a tablet" style="background:linear-gradient(135deg,#e4e7ea,#bfc6cc 55%,#8f9aa4)"></div>
  <h3>Cost Model</h3>
  <p>Build and customize cost models to simulate scenarios, analyze margins, and forecast with confidence.</p>
  <a>More Info.</a>
</div>

<!-- community band -->
<div class="band" style="top:2816px;height:266px;background:linear-gradient(120deg,#1a55a8,#173f86 60%,#1b4c9b)"></div>
<h2 class="abs center" style="top:2880px;font-size:30px;line-height:43px;color:#fff">Where Data Leaders Connect, Collaborate, &amp;<br>Grow Together</h2>
<div class="btn btn-orange" style="left:498px;top:2983px;width:204px;height:36px">Join the community</div>

<!-- who it's for -->
<div class="eyebrow" style="left:145px;top:3221px">IMPACT LEADERS</div>
<h2 class="abs" style="left:145px;top:3245px;font-size:31px">Who Is KOVIL For?</h2>
<p class="abs" style="left:145px;top:3298px;width:420px;font-size:12px;line-height:22.5px;color:var(--muted)">At KOVIL, we believe data should drive meaningful change not just reports. Our platform bridges the gap between complex datasets and real-world outcomes in healthcare and</p>
<svg width="0" height="0" style="position:absolute"><defs><path id="tick" d="M3 7l3 3 6-6" fill="none" stroke="#fff" stroke-width="2"/></defs></svg>
<div class="check" style="left:145px;top:3388px"><i><svg width="14" height="14"><use href="#tick"/></svg></i>Sales managers</div>
<div class="check" style="left:320px;top:3388px"><i><svg width="14" height="14"><use href="#tick"/></svg></i>Real Estate Managers</div>
<div class="check" style="left:145px;top:3424px"><i><svg width="14" height="14"><use href="#tick"/></svg></i>Financials</div>
<div class="check" style="left:320px;top:3424px"><i><svg width="14" height="14"><use href="#tick"/></svg></i>BI Specialists</div>
<div class="btn btn-orange" style="left:143px;top:3482px;width:152px">Learn More</div>
<div class="round-photo" style="left:629px;top:3157px;width:424px;height:424px;background:linear-gradient(135deg,#6f6558,#3d3a36 45%,#d9dde2 60%,#1f5fa8 85%)" role="img" aria-label="Laptop on a wooden desk displaying blue data charts"></div>

<!-- testimonials -->
<div class="eyebrow center" style="top:3672px">Client Testimonials</div>
<h2 class="abs center" style="top:3697px;font-size:30px">Hear From The Data-Driven Leaders Who Trust KOVIL</h2>

<div class="quote" style="left:-169px">"Lorem Ipsum is simply dummy text of the printing and typesetting industry. Lorem Ipsum has been the industry's standard dummy text ever since the 1500s, when an unknown printer took a galley of type and scrambled it to make a type specimen book."
  <div class="mark" style="top:206px;background:var(--blue-deep)">”</div></div>
<div class="quote" style="left:217px">"Lorem Ipsum is simply dummy text of the printing and typesetting industry. Lorem Ipsum has been the industry's standard dummy text ever since the 1500s, when an unknown"
  <div class="who" style="top:160px">Rhea Talbot</div><div class="org" style="top:178px">Northfield Labs</div>
  <div class="mark" style="top:158px;background:var(--orange)">”</div></div>
<div class="quote" style="left:610px">"Lorem Ipsum is simply dummy text of the printing and typesetting industry. Lorem Ipsum has been the industry's standard dummy text ever since the 1500s, when an unknown printer took a galley of type and scrambled it to make a type specimen book."
  <div class="who" style="top:207px">Simon Varga</div><div class="org" style="top:225px">Brightline Systems</div>
  <div class="mark" style="top:206px;background:var(--blue-deep)">”</div></div>
<div class="quote" style="left:998px">"Lorem Ipsum is simply dummy text of the printing and typesetting industry. Lorem Ipsum has been the industry's standard dummy text ever since the 1500s, when an unknown"
  <div class="who" style="top:160px">Leo Marsh</div><div class="org" style="top:178px">Calder Group</div></div>

<!-- cta band -->
<div class="band" style="top:4162px;height:286px;overflow:hidden;background:linear-gradient(100deg,#0c2140,#2a5b96 30%,#0d2450 60%,#0a1b3c)" role="img" aria-label="Night view of the earth with glowing city lights and network lines"></div>
<h2 class="abs" style="left:655px;top:4232px;font-size:30px;line-height:43px;color:#fff">Got Questions? We've<br>Got Insights</h2>
<div class="btn btn-orange" style="left:655px;top:4341px;width:134px">Start KOVIL</div>
<div class="btn btn-outline-light" style="left:803px;top:4341px;width:155px">Plan a Demo</div>

<!-- footer -->
<footer class="abs footer">
  <div class="abs logo" style="left:141px;top:80px;color:#fff">KOVIL</div>
  <p class="abs" style="left:141px;top:128px;width:220px;font-size:12px;line-height:22px;color:#fff">Empowering data-driven decisions through smart tools &amp; community insight</p>
  <span class="abs" style="left:141px;top:198px;width:18px;height:18px;border-radius:50%;background:#fff"></span>

  <h4 style="left:415px;top:80px">Quick Links</h4>
  <ul style="left:415px;top:120px"><li>What is KOVIL?</li><li>Products</li><li>Who It's For</li><li>Community</li><li>About Us</li><li>Contact</li></ul>

  <h4 style="left:587px;top:80px">Contact Us</h4>
  <ul style="left:587px;top:116px;line-height:45px">
    <li style="display:flex;align-items:center;gap:18px"><svg width="26" height="26" viewBox="0 0 26 26"><circle cx="13" cy="13" r="13" fill="rgba(255,255,255,.15)"/><path d="M9 7l3 3-2 2a8 8 0 0 0 4 4l2-2 3 3-2 2c-5 0-10-5-10-10z" fill="#fff"/></svg>(555)-014-2290</li>
    <li style="display:flex;align-items:center;gap:18px"><svg width="26" height="26" viewBox="0 0 26 26"><circle cx="13" cy="13" r="13" fill="rgba(255,255,255,.15)"/><rect x="7" y="9" width="12" height="8" fill="none" stroke="#fff" stroke-width="1.5"/><path d="M7 9l6 5 6-5" fill="none" stroke="#fff" stroke-width="1.5"/></svg>info@kovildata.com</li>
    <li style="display:flex;align-items:center;gap:18px"><svg width="26" height="26" viewBox="0 0 26 26"><circle cx="13" cy="13" r="13" fill="rgba(255,255,255,.15)"/><path d="M13 6a5 5 0 0 0-5 5c0 4 5 9 5 9s5-5 5-9a5 5 0 0 0-5-5z" fill="#fff"/><circle cx="13" cy="11" r="2" fill="#1a4a98"/></svg>info@kovildata.com</li>
  </ul>

  <h4 style="left:865px;top:78px">Subscribe to Newsletter</h4>
  <div class="abs" style="left:865px;top:120px;width:198px;height:38px;border:1px solid rgba(255,255,255,.6);border-radius:19px;font-size:11px;color:rgba(255,255,255,.7);padding:12px 22px">Enter email address</div>
  <div class="btn btn-orange" style="left:865px;top:172px;width:198px">Subscribe Now</div>

  <div class="copyright" style="top:332px">
    <span class="abs" style="left:141px;top:13px">Copyright © 2025 Kovil Healthcare Data Technology | All Rights Reserved.</span>
    <span class="abs" style="right:137px;top:13px">Disclaimer | Privacy Policy | Terms &amp; Conditions</span>
  </div>
</footer>

</body>
</html>
```